Toblero Kids clothing needs two banners for its website

I have uploaded two images which are already 1767*887 in size, i want two website banners created using each image as a separate banner. I need the banners to be playful and with a lot of colors.
We sell kids clothes such as casual shirts, dresses, polo shirts, jeggings , jeans and cargo pants.
Our products are fashionable but with a unique twist. At the moment we are having 30% sale on all our Jackets.
We have just introduced our spring/summer 2014 collections with unique twist.
We also stock a lot of denim stuff too.
You can use the following messages on the banners: (or you come up with some similar messages)
1.)introducing our Stay Bright spring summer 2014 collection.
2.)30% Sale on all Jackets.
3.)Checkout our amazing unique styles: dresses, casual shirts, jeggings, pants, jeans ,cargo pants starting from $15
You can use the following messages on the banners:
PLease note: This project is for two separate banners, each image uploaded should be used for separate designs. Thank you
Kids and their parents
Clothing

```html
<!DOCTYPE html>
<html lang="en">
<head>
<meta charset="UTF-8">
<title>Stay Bright Spring Summer 2014 Collection</title>
<link rel="stylesheet" href="https://fonts.googleapis.com/css2?family=Bebas+Neue&display=swap">
<style>
  :root {
    --page-white: #ffffff;
    --frame-yellow: #fff200;
    --panel-purple: #7b3fb0;
    --panel-purple-light: #a57bd0;
    --headline-yellow: #fff200;
    --headline-shadow: #4e1f7a;
    --photo-teal: #2f8a8c;
    --photo-blue: #4a90c8;
  }
  * { margin: 0; padding: 0; box-sizing: border-box; }
  html, body {
    width: 1200px;
    height: 1000px;
    overflow: hidden;
    background: var(--page-white);
  }
  .canvas {
    position: relative;
    width: 1200px;
    height: 1000px;
    background: var(--page-white);
  }
  .banner {
    position: absolute;
    left: 0;
    top: 200px;
    width: 1200px;
    height: 602px;
    display: flex;
  }
  .photo-frame {
    position: relative;
    width: 579px;
    height: 602px;
    background: var(--frame-yellow);
  }
  .photo-slot {
    position: absolute;
    left: 39px;
    top: 38px;
    width: 540px;
    height: 530px;
    background:
      radial-gradient(ellipse 30% 55% at 38% 52%, rgba(47,138,140,0.35), transparent 70%),
      radial-gradient(ellipse 22% 50% at 72% 52%, rgba(74,144,200,0.35), transparent 70%),
      var(--page-white);
  }
  .message-panel {
    position: relative;
    width: 621px;
    height: 602px;
    background: radial-gradient(circle at 50% 50%, var(--panel-purple-light) 0%, var(--panel-purple) 72%);
  }
  .headline {
    position: absolute;
    left: 0;
    top: 0;
    width: 621px;
    height: 602px;
  }
  .headline text {
    font-family: "Bebas Neue", "Oswald", sans-serif;
    fill: var(--headline-yellow);
    filter: drop-shadow(3px 3px 0 var(--headline-shadow));
  }
</style>
</head>
<body>
  <div class="canvas">
    <section class="banner" aria-label="Spring summer 2014 collection banner">
      <div class="photo-frame">
        <div class="photo-slot" role="img" aria-label="Photo of two smiling kids holding hands, a girl in a teal dress and a boy in a blue shirt with denim shorts"></div>
      </div>
      <div class="message-panel">
        <svg class="headline" viewBox="0 0 621 602" role="heading" aria-level="1" aria-label="Introducing our Stay Bright spring summer 2014 collection">
          <text class="line-intro" x="121" y="228" font-size="100" textLength="378" lengthAdjust="spacingAndGlyphs">INTRODUCING</text>
          <text class="line-name" x="121" y="292" font-size="74" textLength="370" lengthAdjust="spacingAndGlyphs">OUR STAY BRIGHT</text>
          <text class="line-season" x="121" y="345" font-size="56" textLength="368" lengthAdjust="spacingAndGlyphs">SPRING SUMMER 2014</text>
          <text class="line-collection" x="121" y="435" font-size="96" textLength="368" lengthAdjust="spacingAndGlyphs">COLLECTION</text>
        </svg>
      </div>
    </section>
  </div>
</body>
</html>
```